Nourish Kin Collective Australia needs a flyer to update to new style guide and modernise

Nourish Kin Collective Australia (NKCA) is looking to update their flyers. NKCA is a volunteer, parent-led, not for profit organisation that supports and advocates for parents and carers of someone with an eating disorder. Attached is some flyers and brochures that we are currently working with, since producing those we have introduced a style guide, also attached. The flyer needs to be visually appealing and professional.We are hoping to combine the NKCA flyer and NKCA Brochure into a single item. We also need to add in our new Kindle support groups.This would replace the back page of the brochure ("NKCA Will endeavour to facilitate and advocate...) Please refer to last pages of style guide for Kindle details.If the document could be produced to allow changes to wording as certain details will need to be refined or edited in the future.

Target Market(s)

Parents and Carers of someone with a life threatening mental illness

Font styles to use
Other font styles liked:
• Avenir Next

Colors

Designer to choose colors to be used in the design.

Requirements
Must have
• NKCA logos and font matching style guide
Nice to have
• Clean and professional looking design, visually appealing
• Easy to read
Should not have
• Upsetting images

```html
<!DOCTYPE html>
<html lang="en">
<head>
<meta charset="utf-8">
<title>NKCA Flyer – Design Options</title>
<link rel="stylesheet" href="https://fonts.googleapis.com/css2?family=Arimo:wght@400;600;700&family=Luckiest+Guy&display=swap">
<style>
  :root {
    --board: #e6e7e9;
    --purple: #84257a;
    --yellow: #fdd20e;
    --teal: #12a0c8;
    --blue: #4473b8;
    --navy: #26529e;
    --white: #ffffff;
    --display: "Luckiest Guy", "Comic Sans MS", cursive;
    --body: "Arimo", Arial, sans-serif;
  }
  * { box-sizing: border-box; margin: 0; padding: 0; }
  html, body { width: 1200px; height: 849px; overflow: hidden; background: var(--board); }
  .board { position: relative; width: 1200px; height: 849px; }

  .flyer { position: absolute; top: 56px; width: 487px; height: 689px; overflow: hidden; background: var(--yellow); }
  .flyer--one { left: 79px; }
  .flyer--two { left: 633px; }
  .flyer__bg { position: absolute; inset: 0; width: 487px; height: 689px; }

  .web-bar { position: absolute; left: 37px; top: 17px; color: var(--white); font: 700 14.4px/1 var(--body); white-space: nowrap; }
  .web-bar svg { width: 11px; height: 11px; vertical-align: -1px; margin: 0 3px; }

  .headline { position: absolute; left: 36px; top: 72px; color: var(--purple); font: 36px/39.5px var(--display);
    text-shadow: 2px 0 var(--white), -2px 0 var(--white), 0 2px var(--white), 0 -2px var(--white),
                 1.5px 1.5px var(--white), -1.5px -1.5px var(--white), 1.5px -1.5px var(--white), -1.5px 1.5px var(--white); }
  .intro { position: absolute; left: 37px; color: var(--white); font: 400 11.6px/13.4px var(--body); }
  .intro--one { top: 235px; width: 210px; }
  .intro--two { top: 286px; width: 240px; }
  .intro--lead { top: 325px; width: 225px; font-size: 14.6px; line-height: 17.2px; }

  .help-title { position: absolute; left: 49px; top: 408px; color: var(--purple); font: 36px/1 var(--display);
    text-shadow: 2px 0 var(--white), -2px 0 var(--white), 0 2px var(--white), 0 -2px var(--white),
                 1.5px 1.5px var(--white), -1.5px -1.5px var(--white), 1.5px -1.5px var(--white), -1.5px 1.5px var(--white); }

  .help-list { position: absolute; left: 48px; top: 0; list-style: none; }
  .help-list li { position: absolute; left: 0; width: 240px; padding-left: 20px; color: var(--white); font: 400 12.4px/14.4px var(--body); white-space: nowrap; }
  .help-list svg { position: absolute; left: 0; top: 2px; width: 12px; height: 12px; }

  .brand { position: absolute; left: 320px; top: 392px; width: 180px; text-align: center; }
  .brand__mark { display: inline-flex; align-items: center; gap: 6px; color: var(--purple); font: 700 28px/1 var(--body); }
  .brand__dot { width: 22px; height: 22px; border-radius: 50%; background: var(--blue); }
  .brand__name { margin-top: 10px; color: #222; font: 400 9.6px/1.1 var(--body); }

  .join { position: absolute; left: 320px; top: 516px; width: 180px; text-align: center; color: var(--navy); font: 34px/34px var(--display); }

  .social { position: absolute; left: 324px; top: 632px; width: 150px; height: 29px; border-radius: 15px; background: var(--navy);
    color: var(--white); font: 400 10.4px/29px var(--body); padding-left: 34px; white-space: nowrap; box-shadow: 0 6px 10px rgba(0,0,0,.12); }
  .social__dot { position: absolute; left: 0; top: -1px; width: 31px; height: 31px; border-radius: 50%; background: var(--navy); border: 2px solid var(--white); }

  .label { position: absolute; top: 764px; width: 487px; text-align: center; color: var(--navy); font: 700 37px/1 var(--body); }
  .label--one { left: 79px; }
  .label--two { left: 633px; }
</style>
</head>
<body>
<main class="board">

  <!-- Option one -->
  <article class="flyer flyer--one">
    <svg class="flyer__bg" viewBox="0 0 932 1318" preserveAspectRatio="none" aria-hidden="true">
      <defs>
        <linearGradient id="photo-tone-a" x1="0" y1="0" x2="1" y2="1">
          <stop offset="0" stop-color="#3a2620"/><stop offset=".45" stop-color="#b87a5a"/><stop offset="1" stop-color="#ee6a63"/>
        </linearGradient>
      </defs>
      <rect width="932" height="100" fill="var(--purple)"/>
      <circle cx="860" cy="40" r="175" fill="var(--blue)"/>
      <path d="M330 805 C320 560 420 430 600 420 L932 420 L932 1318 L330 1318 Z" fill="var(--purple)"/>
      <path d="M0 805 L600 805 C690 890 700 1000 660 1100 C630 1180 575 1250 585 1318 L0 1318 Z" fill="var(--teal)"/>
      <path d="M560 700 C580 620 680 590 780 640 C840 662 900 640 932 630 L932 1318 L585 1318 C575 1250 630 1180 660 1100 C700 1000 690 890 600 805 C565 770 555 730 560 700 Z" fill="var(--white)"/>
      <path role="img" aria-label="Photo of a young girl happily biting into a burger" d="M440 250 C460 150 560 50 700 45 L932 45 L932 640 C860 660 820 640 780 630 C700 590 620 560 560 470 C500 400 450 330 440 250 Z" fill="url(#photo-tone-a)"/>
    </svg>

    <p class="web-bar">Visit our website now<svg viewBox="0 0 12 12"><path d="M11 1 L1 5 L5 6.5 L6.5 11 Z" fill="#fff"/></svg>www.nourishkin.org.au</p>
    <h1 class="headline">Does your<br>child have<br>an eating<br>disorder?</h1>
    <p class="intro intro--one">Are you concerned your child has a problem with eating, weight or body image?</p>
    <p class="intro intro--two">Parents and carers play a pivotal role in treatment &amp; recovery of eating disorders</p>
    <p class="intro intro--lead">NKCA will help you get the skills &amp; knowledge you need to support your loved one through this illness</p>

    <h2 class="help-title">We can help</h2>
    <ul class="help-list">
      <li style="top:468px"><svg viewBox="0 0 12 12"><circle cx="6" cy="6" r="6" fill="#fff"/><path d="M3.2 6.2 L5.2 8 L8.8 4.2" stroke="var(--teal)" stroke-width="1.6" fill="none"/></svg>NKCA supports families and carers of<br>people with an eating disorder</li>
      <li style="top:510px"><svg viewBox="0 0 12 12"><circle cx="6" cy="6" r="6" fill="#fff"/><path d="M3.2 6.2 L5.2 8 L8.8 4.2" stroke="var(--teal)" stroke-width="1.6" fill="none"/></svg>Early action is imperative</li>
      <li style="top:538px"><svg viewBox="0 0 12 12"><circle cx="6" cy="6" r="6" fill="#fff"/><path d="M3.2 6.2 L5.2 8 L8.8 4.2" stroke="var(--teal)" stroke-width="1.6" fill="none"/></svg>NKCA will help guide you to appropriate<br>resources &amp; support</li>
      <li style="top:581px"><svg viewBox="0 0 12 12"><circle cx="6" cy="6" r="6" fill="#fff"/><path d="M3.2 6.2 L5.2 8 L8.8 4.2" stroke="var(--teal)" stroke-width="1.6" fill="none"/></svg>NKCA advocates for parents/carers to<br>be actively involved in treatment team</li>
      <li style="top:624px"><svg viewBox="0 0 12 12"><circle cx="6" cy="6" r="6" fill="#fff"/><path d="M3.2 6.2 L5.2 8 L8.8 4.2" stroke="var(--teal)" stroke-width="1.6" fill="none"/></svg>NKCA acknowledges the importance of<br>well-being of ALL family members<br>throughout the ED journey</li>
    </ul>

    <div class="brand">
      <div class="brand__mark"><span class="brand__dot"></span>NKCA</div>
      <p class="brand__name">Nourish Kin Collective Australia</p>
    </div>
    <p class="join">Join<br>us<br>today!</p>
    <p class="social"><span class="social__dot"></span>@nourishkincollective</p>
  </article>

  <!-- Option two -->
  <article class="flyer flyer--two">
    <svg class="flyer__bg" viewBox="0 0 932 1318" preserveAspectRatio="none" aria-hidden="true">
      <defs>
        <linearGradient id="photo-tone-b" x1="0" y1="0" x2="1" y2="1">
          <stop offset="0" stop-color="#3a2620"/><stop offset=".45" stop-color="#b87a5a"/><stop offset="1" stop-color="#ee6a63"/>
        </linearGradient>
      </defs>
      <rect width="932" height="100" fill="var(--purple)"/>
      <circle cx="860" cy="40" r="175" fill="var(--blue)"/>
      <path d="M330 805 C320 560 420 430 600 420 L932 420 L932 1318 L330 1318 Z" fill="var(--purple)"/>
      <path d="M0 805 L330 805 C360 900 420 960 480 1010 C560 1080 580 1180 510 1318 L0 1318 Z" fill="var(--teal)"/>
      <path d="M560 700 C580 620 680 590 780 640 C840 662 900 640 932 630 L932 1318 L585 1318 C575 1250 630 1180 660 1100 C700 1000 690 890 600 805 C565 770 555 730 560 700 Z" fill="var(--white)"/>
      <path role="img" aria-label="Photo of a young girl happily biting into a burger" d="M440 250 C460 150 560 50 700 45 L932 45 L932 640 C860 660 820 640 780 630 C700 590 620 560 560 470 C500 400 450 330 440 250 Z" fill="url(#photo-tone-b)"/>
    </svg>

    <p class="web-bar">Visit our website now<svg viewBox="0 0 12 12"><path d="M11 1 L1 5 L5 6.5 L6.5 11 Z" fill="#fff"/></svg>www.nourishkin.org.au</p>
    <h1 class="headline">Does your<br>child have<br>an eating<br>disorder?</h1>
    <p class="intro intro--one">Are you concerned your child has a problem with eating, weight or body image?</p>
    <p class="intro intro--two">Parents and carers play a pivotal role in treatment &amp; recovery of eating disorders</p>
    <p class="intro intro--lead">NKCA will help you get the skills &amp; knowledge you need to support your loved one through this illness</p>

    <h2 class="help-title">We can help</h2>
    <ul class="help-list">
      <li style="top:468px"><svg viewBox="0 0 12 12"><circle cx="6" cy="6" r="6" fill="#fff"/><path d="M3.2 6.2 L5.2 8 L8.8 4.2" stroke="var(--teal)" stroke-width="1.6" fill="none"/></svg>NKCA supports families and carers of<br>people with an eating disorder</li>
      <li style="top:510px"><svg viewBox="0 0 12 12"><circle cx="6" cy="6" r="6" fill="#fff"/><path d="M3.2 6.2 L5.2 8 L8.8 4.2" stroke="var(--teal)" stroke-width="1.6" fill="none"/></svg>Early action is imperative</li>
      <li style="top:538px"><svg viewBox="0 0 12 12"><circle cx="6" cy="6" r="6" fill="#fff"/><path d="M3.2 6.2 L5.2 8 L8.8 4.2" stroke="var(--teal)" stroke-width="1.6" fill="none"/></svg>NKCA will help guide you to appropriate<br>resources &amp; support</li>
      <li style="top:581px"><svg viewBox="0 0 12 12"><circle cx="6" cy="6" r="6" fill="#fff"/><path d="M3.2 6.2 L5.2 8 L8.8 4.2" stroke="var(--teal)" stroke-width="1.6" fill="none"/></svg>NKCA advocates for parents/carers to<br>be actively involved in treatment team</li>
      <li style="top:624px"><svg viewBox="0 0 12 12"><circle cx="6" cy="6" r="6" fill="#fff"/><path d="M3.2 6.2 L5.2 8 L8.8 4.2" stroke="var(--teal)" stroke-width="1.6" fill="none"/></svg>NKCA acknowledges the importance of<br>well-being of ALL family members<br>throughout the ED journey</li>
    </ul>

    <div class="brand">
      <div class="brand__mark"><span class="brand__dot"></span>NKCA</div>
      <p class="brand__name">Nourish Kin Collective Australia</p>
    </div>
    <p class="join">Join<br>us<br>today!</p>
    <p class="social"><span class="social__dot"></span>@nourishkincollective</p>
  </article>

  <p class="label label--one">Design 01</p>
  <p class="label label--two">Design 02</p>
</main>
</body>
</html>
```